Mortgage Protection Insurance Flyer

The target audience are new home owners so the design needs to be clean and simple.

This a primarily for Final Expense Insurance, but need an area where it says "We Also Specialize In:"
- Medicare Supplement Insurance (MediGap)
- Annuities
- Final Expense

All flyer versions need to be editable. Colors to be used are red, white or black. Refer to my website for colors and photos (harborvaleassurance.com). Will attach my logo and a flyer that I found online that is the format that I am looking for (for 8.5 in. x 11 in version). Need flyer in standard letter size 8.5 in. x11 in. but also in 8.5 in. x 5.5 in and 5.0 in. x 8.0 in. All sizes to be portrait oriented. If picked as winning design, need all flyer versions in full color, also in grey scale and files in all industry file types.

Content can be taken from my website..... harborvaleassurance.com

Do NOT submit if you are not willing to provide all versions as described above for the original project price.

Must use royalty-free stock photos please.

Target Market(s)

New homeowners looking for insurance to protect there mortgage payments

Industry/Entity Type

Life Insurance

Colors
f69fa3

Requirements
Must have
• Colors to be used are red, white or black.
• Need flyer in standard letter size 8.5 in. x11 in. but also in 3.5 in. x 8.5 in (Full Bleed 3.75 in by 8.75 in.) and 4.0 in. x 6.0 in. (Full Bleed 4.12 in x 6.12 in) Each design tailored to the size dimensions (So no squeezing 8.5 x 11 design into a 4.0 x 6.0 space.) All sizes to be portrait oriented. If picked as winning design, need all flyer versions in full color, also in grey scale and files in all file types.
• Do not need physical address on flyer, do need email address on flyer though - tkerlow@harborvaleassurance.com
• So phone number should be prominent, email address and website address should also be contact area.
• If you can not agree to terms above, do not submit any designs.
• Need facebook & twitter logos somewhere in contact info area.
Nice to have
• See sample flyers I have attached.
• White background with red used as primary graphic color and black used as secondary graphic if needed.
• font to be used should similar to one used in logo.

```html
<!DOCTYPE html>
<html lang="en">
<head>
<meta charset="utf-8">
<title>Harborvale Assurance – Flyer</title>
<link href="https://fonts.googleapis.com/css2?family=Montserrat:wght@400;500;600;700;800&display=swap" rel="stylesheet">
<style>
  :root{
    --backdrop:#b7b2b3;
    --paper:#f1f1f1;
    --red:#c8161d;
    --black:#141414;
    --ink:#222222;
    --white:#ffffff;
  }
  *{margin:0;padding:0;box-sizing:border-box}
  html,body{width:900px;height:1200px;overflow:hidden;background:var(--backdrop);font-family:"Montserrat",sans-serif;color:var(--ink)}
  .flyer{position:absolute;left:43px;top:72px;width:817px;height:1056px;background:var(--paper);box-shadow:6px 6px 8px rgba(0,0,0,.45);overflow:hidden}
  .flyer-art{position:absolute;left:0;top:0;width:817px;height:1056px}
  .headline{position:absolute;left:17px;top:666px;font-size:28.5px;font-weight:700;color:var(--black);letter-spacing:.1px}
  .headline-rule{position:absolute;left:17px;top:708px;width:65px;height:7px;border-radius:4px;background:var(--black);overflow:hidden}
  .headline-rule::before{content:"";position:absolute;left:0;top:0;width:32px;height:7px;background:var(--red)}
  .intro{position:absolute;left:17px;top:726px;width:790px;font-size:12px;font-weight:700;line-height:1.35;color:var(--black)}
  .service{position:absolute;left:15px;width:790px}
  .service-title{font-size:14.5px;font-weight:700;color:var(--red);margin-bottom:6px}
  .service-text{font-size:11.4px;line-height:1.34;color:var(--ink)}
  .service--final{top:774px}
  .service--medigap{top:836px}
  .specialties{position:absolute;left:15px;top:932px;width:790px;display:flex;align-items:center;gap:14px;font-size:11.6px;color:var(--ink)}
  .specialties-title{font-weight:700;color:var(--red);font-size:12.5px}
  .specialties ul{list-style:none;display:flex;gap:14px}
  .specialties li{display:flex;align-items:center;gap:6px;font-weight:600}
  .specialties li::before{content:"";width:6px;height:6px;border-radius:50%;background:var(--red)}
  .contact{position:absolute;left:17px;top:968px;color:var(--white)}
  .contact-phone{font-size:25px;font-weight:500;white-space:nowrap;line-height:1.1}
  .contact-phone strong{font-size:31px;font-weight:700}
  .contact-line{margin-top:6px;font-size:13.5px;font-weight:500;display:flex;align-items:center;gap:8px;white-space:nowrap}
  .social{display:flex;gap:6px;margin-left:8px}
  .social span{width:16px;height:16px;border-radius:50%;background:var(--white)}
  .brand{position:absolute;left:479px;top:978px;width:338px;text-align:center;font-size:27px;font-weight:800;color:var(--black);letter-spacing:1px;line-height:1.1}
</style>
</head>
<body>
<main class="flyer">
  <svg class="flyer-art" viewBox="0 0 817 1056" xmlns="http://www.w3.org/2000/svg">
    <defs>
      <linearGradient id="familyTone" x1="0" y1="0" x2="1" y2="1">
        <stop offset="0" stop-color="#c99a4d"/>
        <stop offset=".45" stop-color="#8a7a5a"/>
        <stop offset="1" stop-color="#4e6f93"/>
      </linearGradient>
      <linearGradient id="adviceTone" x1="0" y1="0" x2="1" y2="1">
        <stop offset="0" stop-color="#b9bcc0"/>
        <stop offset="1" stop-color="#3b4a66"/>
      </linearGradient>
      <linearGradient id="homeTone" x1="0" y1="0" x2="0" y2="1">
        <stop offset="0" stop-color="#a2775c"/>
        <stop offset="1" stop-color="#3f4f6d"/>
      </linearGradient>
    </defs>
    <path d="M0,0 H612 Q680,90 665,200 L560,600 Q300,660 0,560 Z" fill="url(#familyTone)" role="img" aria-label="Photo: smiling multi-generation family outdoors in warm sunlight"/>
    <path d="M612,0 Q680,90 668,200" fill="none" stroke="var(--red)" stroke-width="3"/>
    <path d="M0,558 Q250,660 520,600 L470,640 Q250,690 0,610 Z" fill="var(--red)"/>
    <circle cx="650" cy="313" r="128" fill="var(--white)"/>
    <circle cx="650" cy="313" r="124" fill="url(#adviceTone)" stroke="var(--red)" stroke-width="3" role="img" aria-label="Photo: advisor reviewing a document with a client"/>
    <circle cx="563" cy="513" r="128" fill="var(--white)"/>
    <circle cx="563" cy="513" r="124" fill="url(#homeTone)" stroke="var(--red)" stroke-width="3" role="img" aria-label="Photo: young couple and child sitting on the steps of their new home"/>
    <polygon points="0,963 419,963 457,1056 0,1056" fill="var(--red)"/>
    <polygon points="425,963 441,963 479,1056 463,1056" fill="var(--black)"/>
    <rect x="479" y="1050" width="338" height="6" fill="var(--black)"/>
  </svg>

  <h1 class="headline">OUR PLANS ARE BASED ON YOURS</h1>
  <div class="headline-rule"></div>
  <p class="intro">Get the right Final Expense Insurance, Medicare Supplement Insurance or Mortgage Protection Insurance plan for your family's peace-of-mind!</p>

  <section class="service service--final">
    <h2 class="service-title">Final Expense Insurance</h2>
    <p class="service-text">Final Expense Insurance is a type of permanent life insurance where the death benefit is used to cover (but not limited to) medical costs, funeral costs and other end-of-life expenses. It is a budget friendly option with a death benefit of up to $35k.</p>
  </section>

  <section class="service service--medigap">
    <h2 class="service-title">Medicare Supplement Insurance (MediGap)</h2>
    <p class="service-text">Medicare Supplement Insurance (also called MediGap) helps pay the “gap” between what Original Medicare (Medicare Parts A and B) pays and what you pay out of your own pocket. There are up to 10 different "MediGap" basic benefits options to choose from. Plans are labeled A, B, C, D, F, G, K, L, M, and N. Confusing? It can be. This is where we come in. We explain and help you find the right plan that fits your budget.</p>
  </section>

  <section class="specialties">
    <h2 class="specialties-title">We Also Specialize In:</h2>
    <ul>
      <li>Medicare Supplement Insurance (MediGap)</li>
      <li>Annuities</li>
      <li>Final Expense</li>
    </ul>
  </section>

  <div class="contact">
    <p class="contact-phone">Call Us: <strong>(208)555.0147</strong></p>
    <p class="contact-line">
      <svg width="16" height="12" viewBox="0 0 16 12" aria-hidden="true"><rect x="1" y="1" width="14" height="10" fill="none" stroke="#fff" stroke-width="1.6"/><path d="M1 1l7 6 7-6" fill="none" stroke="#fff" stroke-width="1.6"/></svg>
      tkerlow@harborvaleassurance.com
    </p>
    <p class="contact-line">
      <svg width="16" height="16" viewBox="0 0 16 16" aria-hidden="true"><circle cx="8" cy="8" r="6.5" fill="none" stroke="#fff" stroke-width="1.5"/><path d="M1.5 8h13M8 1.5c-3 3.5-3 9.5 0 13M8 1.5c3 3.5 3 9.5 0 13" fill="none" stroke="#fff" stroke-width="1.2"/></svg>
      harborvaleassurance.com
      <span class="social" aria-label="Social media"><span></span><span></span></span>
    </p>
  </div>

  <div class="brand">HARBORVALE<br>ASSURANCE</div>
</main>
</body>
</html>
```